Business card for consulting firm

We need a double-sided business card for consulting firm, VantorQ. The card should be professional but also creative and visually interesting.

Target Market(s)

Engineering and technology; transport industries; safety critical / heavy industry.

Contact Information for Business Card

See attached file with details.

Font styles to use
Sans Serif

```html
<!DOCTYPE html>
<html lang="en">
<head>
<meta charset="utf-8">
<title>VantorQ Business Card</title>
<link rel="stylesheet" href="https://fonts.googleapis.com/css2?family=Lato:wght@400;700&display=swap">
<style>
  :root {
    --stage: #e4e4e4;
    --card-dark: #000000;
    --card-light: #ffffff;
    --brand-blue: #29b6e6;
    --brand-navy: #13233a;
    --text-white: #ffffff;
    --globe-dark-a: #2a2d30;
    --globe-dark-b: #15171a;
    --globe-light-a: #eef0f2;
    --globe-light-b: #f7f8f9;
  }
  * { box-sizing: border-box; margin: 0; padding: 0; }
  html, body { width: 1200px; height: 1000px; overflow: hidden; }
  body {
    position: relative;
    background: var(--stage);
    font-family: "Lato", Arial, sans-serif;
  }
  .card {
    position: absolute;
    width: 700px;
    height: 420px;
    overflow: hidden;
  }
  .card--front { left: 55px; top: 66px; background: var(--card-dark); }
  .card--back { left: 427px; top: 520px; background: var(--card-light); }

  .globe {
    position: absolute;
    border-radius: 50%;
  }
  .card--front .globe {
    left: 442px; top: -80px; width: 300px; height: 300px;
    background: radial-gradient(circle at 45% 40%, var(--globe-dark-a), var(--globe-dark-b));
  }
  .card--back .globe {
    left: -10px; top: -60px; width: 315px; height: 315px;
    background: radial-gradient(circle at 50% 40%, var(--globe-light-a), var(--globe-light-b));
  }

  .brand { position: absolute; text-align: right; }
  .brand__name {
    display: block;
    font-weight: 700;
    font-size: 56px;
    line-height: 1;
    letter-spacing: 1px;
  }
  .brand__tagline {
    display: block;
    font-weight: 400;
    font-size: 19px;
    letter-spacing: 0.4px;
    margin-top: 4px;
  }
  .card--front .brand { left: 50px; top: 306px; width: 305px; color: var(--text-white); }
  .card--back .brand { left: 355px; top: 64px; width: 305px; color: var(--brand-navy); }

  .contact {
    position: absolute;
    left: 42px;
    top: 303px;
    list-style: none;
    color: var(--brand-navy);
    font-weight: 700;
    font-size: 15px;
    line-height: 21px;
  }
  .contact__item { display: flex; align-items: center; gap: 7px; }
  .contact__icon { width: 13px; height: 13px; flex: none; }
  .contact__item--plain { padding-left: 20px; }

  .person {
    position: absolute;
    right: 39px;
    top: 333px;
    text-align: right;
    color: var(--brand-navy);
  }
  .person__name { font-size: 18px; font-weight: 400; color: var(--brand-blue); line-height: 22px; }
  .person__creds { font-size: 11px; line-height: 16px; }
  .person__role { font-size: 12.5px; font-weight: 700; line-height: 17px; }
  .accent-bar {
    position: absolute;
    right: 0; top: 335px;
    width: 27px; height: 50px;
    background: var(--brand-blue);
  }
</style>
</head>
<body>
  <section class="card card--front">
    <div class="globe" role="img" aria-label="Decorative dotted sphere pattern"></div>
    <div class="brand">
      <span class="brand__name">VANTORQ</span>
      <span class="brand__tagline">Safety &amp; Human Factors</span>
    </div>
  </section>

  <section class="card card--back">
    <div class="globe" role="img" aria-label="Decorative dotted sphere pattern"></div>
    <div class="brand">
      <span class="brand__name">VANTORQ</span>
      <span class="brand__tagline">Safety &amp; Human Factors</span>
    </div>

    <ul class="contact">
      <li class="contact__item">
        <svg class="contact__icon" viewBox="0 0 16 16" aria-hidden="true"><path fill="#29b6e6" d="M3.5 1l2.5 3-1.5 1.8c.8 1.8 2.2 3.2 4 4L10.3 8.5l3 2.5-1.3 2.7c-5.2.3-10-4.5-10.2-10.2z"/></svg>
        +61 (0)400 555 018
      </li>
      <li class="contact__item">
        <svg class="contact__icon" viewBox="0 0 16 16" aria-hidden="true"><rect x="1" y="3" width="14" height="10" rx="1" fill="#29b6e6"/><path d="M1.5 4l6.5 5 6.5-5" stroke="#fff" stroke-width="1.3" fill="none"/></svg>
        hmarsh@vantorq.com.au
      </li>
      <li class="contact__item">
        <svg class="contact__icon" viewBox="0 0 16 16" aria-hidden="true"><g fill="none" stroke="#29b6e6" stroke-width="1.4"><circle cx="8" cy="8" r="6.5"/><ellipse cx="8" cy="8" rx="3" ry="6.5"/><path d="M1.5 8h13"/></g></svg>
        www.vantorq.global
      </li>
      <li class="contact__item contact__item--plain">www.vantorq.com.au</li>
    </ul>

    <div class="person">
      <p class="person__name">HELENA MARSH</p>
      <p class="person__creds">BA (Hons), M Psych Org, M Tech Mgt (HF)</p>
      <p class="person__role">Managing Director</p>
    </div>
    <div class="accent-bar"></div>
  </section>
</body>
</html>
```